Kelvane Plumbing Business cards

Company is Kelvane Plumbing.
name Dashel Morrowby, I am a plumber, drainer, gasfitter and roofer
Mobile: 0431 906 154
Email address: info@kelvaneplumbing.example (check out my website for some ideas)
Website: www.kelvaneplumbing.example
ABN: 82 916 203 471
LIC: 604517K

I am reliable all round plumber. I am a 24 hour emergency service. Kelvane Plumbing is a professional plumbing service in the Illawarra, South Coast, Southern Sydney and Southern Highland regions of NSW. We offer a 24 hour emergency service for piece of mind to our customers. Call us now to see how we can help you. Kelvane Plumbing approaches every job with attention to detail and excellent customer service. With our superior workmanship you can be confident that the job will be done right the first time around. You can rest assured with results that are guaranteed to last.

Target Market(s)

the general public

Contact Information for Business Card

look up website for some ideas something with similar colours to logo and new modern and to catch the eye.

Colors
fdfdfd
ffffff
000000
7f7f7f
aaaaaa
33a6d7
0492cd

Requirements
Must have
• all contact details
• company- Kelvane Plumbing
• name- Dashel Morrowby
• number mobile- 0431 906 154
• Email address- info@kelvaneplumbing.example
• Website- www.kelvaneplumbing.example
• ABN- 82 916 203 471
• LIC- 604517K

```html
<!DOCTYPE html>
<html lang="en">
<head>
<meta charset="utf-8">
<title>Kelvane Plumbing Business Cards</title>
<link href="https://fonts.googleapis.com/css2?family=Lato:wght@400;700&display=swap" rel="stylesheet">
<style>
  :root {
    --backdrop: #1c1c1e;
    --brand-blue: #0492cd;
    --accent-blue: #33a6d7;
    --grey: #7f7f7f;
    --light-grey: #aaaaaa;
    --paper: #fdfdfd;
    --white: #ffffff;
    --ink: #000000;
  }
  * { margin: 0; padding: 0; box-sizing: border-box; }
  html, body {
    width: 1200px;
    height: 912px;
    overflow: hidden;
    background: var(--backdrop);
    font-family: "Lato", sans-serif;
  }
  .card {
    position: absolute;
    width: 680px;
    height: 388px;
    overflow: hidden;
  }

  /* Front card */
  .card-front {
    left: 120px;
    top: 50px;
    background: var(--brand-blue);
    color: var(--white);
  }
  .front-brand {
    position: absolute;
    left: 0;
    right: 0;
    top: 150px;
    display: flex;
    align-items: center;
    justify-content: center;
    gap: 18px;
  }
  .brand-ring {
    width: 46px;
    height: 46px;
    border: 6px solid var(--white);
    border-radius: 50%;
  }
  .front-brand .brand-name {
    font-size: 44px;
    font-weight: 700;
    letter-spacing: 1px;
    color: var(--white);
  }
  .front-website {
    position: absolute;
    right: 56px;
    bottom: 40px;
    font-size: 19px;
    letter-spacing: 0.5px;
  }

  /* Back card */
  .card-back {
    left: 400px;
    top: 474px;
    background: var(--paper);
    color: var(--ink);
  }
  .back-waves {
    position: absolute;
    inset: 0;
  }
  .back-brand {
    position: absolute;
    left: 40px;
    top: 80px;
    display: flex;
    align-items: center;
    gap: 14px;
  }
  .back-brand .brand-ring {
    width: 40px;
    height: 40px;
    border: 6px solid var(--grey);
  }
  .back-brand .brand-name {
    font-size: 30px;
    font-weight: 700;
    color: var(--brand-blue);
  }
  .holder {
    position: absolute;
    right: 40px;
    top: 100px;
    text-align: right;
  }
  .holder-name {
    font-size: 30px;
    font-weight: 700;
    color: var(--brand-blue);
    line-height: 1.1;
  }
  .holder-role {
    font-size: 16px;
    margin-top: 2px;
  }
  .divider {
    position: absolute;
    left: 40px;
    right: 36px;
    top: 206px;
    height: 2px;
    background: var(--brand-blue);
  }
  .registrations {
    position: absolute;
    right: 40px;
    top: 226px;
    text-align: right;
    font-size: 18px;
    line-height: 1.35;
  }
  .contacts {
    position: absolute;
    left: 48px;
    top: 226px;
    list-style: none;
    font-size: 20px;
    line-height: 1.45;
  }
  .contacts li {
    display: flex;
    align-items: center;
    gap: 12px;
  }
  .contacts svg { width: 18px; height: 18px; flex: none; }
  .back-website {
    position: absolute;
    right: 30px;
    bottom: 24px;
    color: var(--white);
    font-size: 17px;
    letter-spacing: 0.3px;
    line-height: 1.2;
  }
</style>
</head>
<body>

<section class="card card-front">
  <div class="front-brand">
    <span class="brand-ring"></span>
    <span class="brand-name">Kelvane Plumbing</span>
  </div>
  <p class="front-website">www.kelvaneplumbing.example</p>
</section>

<section class="card card-back">
  <svg class="back-waves" viewBox="0 0 680 388" aria-hidden="true">
    <path d="M0,352 L330,352 C360,352 378,326 400,306 L394,318 C372,340 356,362 330,362 L0,362 Z" fill="#7f7f7f"/>
    <path d="M0,372 L360,372 C400,372 410,314 460,314 L680,314 L680,388 L0,388 Z" fill="#0492cd"/>
  </svg>

  <div class="back-brand">
    <span class="brand-ring"></span>
    <span class="brand-name">Kelvane Plumbing</span>
  </div>

  <div class="holder">
    <p class="holder-name">Dashel Morrowby</p>
    <p class="holder-role">Plumber</p>
  </div>

  <div class="divider"></div>

  <ul class="contacts">
    <li>
      <svg viewBox="0 0 18 18" aria-hidden="true"><rect x="5" y="1.5" width="8" height="15" rx="1.5" fill="none" stroke="#0492cd" stroke-width="1.5"/><circle cx="9" cy="14" r="0.9" fill="#0492cd"/></svg>
      <span>0431 906 154</span>
    </li>
    <li>
      <svg viewBox="0 0 18 18" aria-hidden="true"><rect x="1.5" y="4" width="15" height="10" fill="#0492cd"/><path d="M1.5,4 L9,10 L16.5,4" fill="none" stroke="#ffffff" stroke-width="1.2"/></svg>
      <span>info@kelvaneplumbing.example</span>
    </li>
  </ul>

  <div class="registrations">
    <p>ABN- 82 916 203 471</p>
    <p>LIC- 604517K</p>
  </div>

  <p class="back-website">www.kelvaneplumbing.example</p>
</section>

</body>
</html>
```